Company Business Card Design Project - Revamp the image of an old construction company.

We need a business card designed for a new company in Australia.

Type of business is Commercial Roofing & Painting.

Medium will be brushed black metal card that can/will be acid etched to a brushed steel silver, acid die cut and two printed colours of our choice which will be white and pantone orange.

We have hopes that the design will be simple, modern and represent with a quick glance what our company does.

Please read instructions carefully in must have box any questions please ask.

If you are interested in this job please look at other job that we have which is very similar with logo and design

Please have a look at the things that can be done with metals cards on google images for inspiration.

Target Market(s)

Business owners, commercial property development Men from 25-70 years of age.

Industry/Entity Type

Construction

Requirements
Must have
• Front of card:

Must use the company logo and name provided as attachment (see below norwick vale construction_black_background).

the words -Commercial Painting and Roofing- must be on front of card

details needed on front or back depending on your design

Name
position
email
mobile

all details can be on front with a cool design to be etched on the back of card or to keep front simple you can put all detail on back of card, I will leave the lay out to you.

Colours in logo are

Pantone 144 C Orange
Pantone 11-0601 White
Pantone 7539 C Gray
Pantone 426 C Black

However black will be the base of black metal card. Gray will be replaced with the etching in card revealing the silver. Orange and white will be printed on card.

Please have fun!!
Should not have
• Please don't clutter the card
No fonts smaller then 7 points

```html
<!DOCTYPE html>
<html lang="en">
<head>
<meta charset="utf-8">
<title>Norwick Vale Construction – Business Card</title>
<link href="https://fonts.googleapis.com/css2?family=Exo+2:wght@400;600;800&family=Roboto+Condensed:wght@400;700&display=swap" rel="stylesheet">
<style>
  :root {
    --bg: #1c1c1c;
    --card-black: #141414;
    --card-grey: #4b4b4b;
    --orange: #f58220;
    --white: #f2f2f2;
    --silver-light: #bdbdbd;
    --silver-dark: #6e6e6e;
  }
  * { margin: 0; padding: 0; box-sizing: border-box; }
  html, body { width: 1200px; height: 1000px; overflow: hidden; background: var(--bg); }
  body { position: relative; font-family: "Roboto Condensed", sans-serif; color: var(--white); }

  .card {
    position: absolute;
    width: 540px;
    height: 310px;
    border-radius: 6px;
    overflow: hidden;
    box-shadow: 0 18px 40px rgba(0,0,0,.55);
  }
  .card--front { left: 50px; top: 110px; background: var(--card-black); }
  .card--back  { left: 610px; top: 480px; background: var(--card-grey); }

  /* brand block */
  .brand { position: absolute; display: flex; align-items: flex-start; gap: 12px; }
  .card--front .brand { left: 60px; top: 105px; }
  .card--back .brand { right: 30px; top: 40px; transform: scale(.72); transform-origin: right top; }
  .brand__mark { width: 22px; height: 22px; background: var(--orange); margin-top: 24px; flex: none; }
  .brand__tagline {
    font-family: "Exo 2", sans-serif; font-weight: 600; font-size: 14px;
    color: var(--white); letter-spacing: .3px;
  }
  .brand__name {
    font-family: "Exo 2", sans-serif; font-weight: 800; font-size: 34px;
    color: var(--orange); text-transform: uppercase; line-height: 1.05; margin-top: 4px;
  }

  /* contact block */
  .person { position: absolute; left: 34px; top: 42px; }
  .person__name { font-weight: 700; font-size: 17px; letter-spacing: .5px; color: var(--white); }
  .person__role { font-weight: 700; font-size: 10px; color: var(--orange); margin-top: 2px; }

  .contact { position: absolute; left: 34px; top: 104px; list-style: none; font-size: 13px; color: var(--white); }
  .contact__item { display: flex; align-items: flex-start; gap: 12px; line-height: 17px; }
  .contact__item + .contact__item { margin-top: 6px; }
  .contact__group { margin-top: 14px; }
  .contact__icon { width: 11px; height: 14px; flex: none; margin-top: 2px; fill: var(--orange); }

  .accent-band {
    position: absolute; left: 0; bottom: 0; width: 230px; height: 8px;
    background: var(--orange);
    clip-path: polygon(0 0, 96% 0, 100% 100%, 0 100%);
  }

  .illustration-area {
    position: absolute; right: 20px; bottom: 0; width: 250px; height: 140px;
    background: linear-gradient(180deg, var(--silver-light) 0%, var(--silver-dark) 100%);
    opacity: .6;
  }
</style>
</head>
<body>

<section class="card card--front" aria-label="Card front">
  <div class="brand">
    <span class="brand__mark"></span>
    <div>
      <p class="brand__tagline">Commercial Painting &amp; Roofing</p>
      <p class="brand__name">Norwick Vale<br>Construction</p>
    </div>
  </div>
</section>

<section class="card card--back" aria-label="Card back">
  <div class="person">
    <p class="person__name">NAME SURNAME</p>
    <p class="person__role">CEO</p>
  </div>

  <ul class="contact">
    <li class="contact__item">
      <svg class="contact__icon" viewBox="0 0 12 16"><path d="M6 0a6 6 0 0 0-6 6c0 4.5 6 10 6 10s6-5.5 6-10a6 6 0 0 0-6-6zm0 8.5A2.5 2.5 0 1 1 6 3.5a2.5 2.5 0 0 1 0 5z"/></svg>
      <span>118 Harbour Lane<br>Eastfield</span>
    </li>
    <li class="contact__item contact__group">
      <svg class="contact__icon" viewBox="0 0 12 16"><path d="M2 0h8a1.5 1.5 0 0 1 1.5 1.5v13A1.5 1.5 0 0 1 10 16H2A1.5 1.5 0 0 1 .5 14.5v-13A1.5 1.5 0 0 1 2 0zm0 2v10h8V2zm4 11a1 1 0 1 0 0 2 1 1 0 0 0 0-2z"/></svg>
      <span>+(61) 400 555 017</span>
    </li>
    <li class="contact__item">
      <svg class="contact__icon" viewBox="0 0 14 14"><path d="M3 1l2 3-1.5 1.5a8 8 0 0 0 5 5L10 9l3 2-1 2.5C6 13.5.5 8 .5 2z"/></svg>
      <span>+(61) 400 555 017</span>
    </li>
    <li class="contact__item contact__group">
      <svg class="contact__icon" viewBox="0 0 14 14"><circle cx="7" cy="7" r="6"/></svg>
      <span>www.norwickvale.com</span>
    </li>
    <li class="contact__item">
      <svg class="contact__icon" viewBox="0 0 14 12"><path d="M0 1h14v10H0zm1.5 1.5L7 7l5.5-4.5z"/></svg>
      <span>hello@norwickvale.com</span>
    </li>
  </ul>

  <div class="brand">
    <span class="brand__mark"></span>
    <div>
      <p class="brand__tagline">Commercial Painting &amp; Roofing</p>
      <p class="brand__name">Norwick Vale<br>Construction</p>
    </div>
  </div>

  <div class="illustration-area" role="img" aria-label="Etched silver illustration of tall commercial buildings"></div>
  <div class="accent-band"></div>
</section>

</body>
</html>
```